Cheese Company Needs Product Label Design

Hello Designers. We are a cheese manufacturer and are looking for a label design for our new product "Fresh Mozzarella". The cheese balls come in a container that includes Sun-Dried Tomato with Parsley and Garlic marinated in oil.Here are the requirements:

1. LABEL: There will be a main circular label and a side label. The main circular label should be 3.83" in diameter. The side rectangular label should be 1.5" Length 3.25" Width.

2. DESIGN (LOGO): The company logo (attached) should be placed on the top in middle just like in the "product example" file that is included in the project.

3. DESIGN (PRODUCT NAME): The product name "FRESH MOZZARELLA" should be below the logo and be big in capital letters straight. Also include "ALL NATURAL" right above the name just like the "product example". Include "ORGANIC" icon somewhere on it.

4. DESIGN (PRODUCT DESCRIPTION): The product description "SUN-DRIED TOMATO and PARSLEY" should be below the product name. Make it look fancy.

5. DESIGN (PRODUCT PICTURE): I would like you to create a product drawing of many mozzarella balls with Sun-Dried Tomato and Parsley in it below the product description. Make sure it is attractive and pops-out on the label. Look at the "product example" to get an idea but please make sure you don't make it exactly the same. This is important as it needs to be arranged in such a way to not be too similar. Look at the file "inspiration 4" to see how it looks like.

6. DESIGN (BACKGROUND): The background of the picture should reflect a natural, organic, elegant scene. Think mountains, valleys, rivers flowing, nature, cows in the field and sun shining. I attached an "inspiration" photos here so you can get an idea. Make sure that the product is the main focus and not the background. It should be sophisticated with not too much color. Include a small border around the whole label.
DO NOT MAKE IT LOOK CARTOONISH!

7. WEIGHT: The weight of the product should be in the lower right corner and should say "NET WT. 12oz" and below that "(340g)".

8. KOSHER: The tablet kosher symbol should be on the lower right corner. Please look it up how it looks like.

9. SIDE LABEL: The side label should maintain the same color scheme as the main label similar to the "product example" attached here. It should have the Nutritional Facts attached, the Bar Code, and the "DISTRIBUTED BY: BRAVOLT LLC. 482 ELMCREST AVENUE, GLEN HARBOR, NY 11592". You can arrange it how you see fit but the Bar Code should be at least 1/3 of the label. Refer to the "product example" and keep close to its design. Put "MADE IN USA" on the right hand side. The last few things you need to do is put the Ingredients List below the Nutritional Facts as shown in the "product example", put the website "WWW.BRAVOLTFOODS.COM" below the Ingredients List, and put three social media icons going Facebook, Twitter, Instagram referring to @BravoltFoods somewhere near the bottom in it. Put the plant number on the side "PLANT NO. 52-7049" on it. Type out on the same side in bold letters to "KEEP REFRIGERATED".

10. FINAL: Thank you for accepting this project. As a main objective the label needs to look sophisticated and a high quality product. You can add your own twist on the design and keep it close to the rules. The Bar Code is not included in the files and will be given once we choose you as a designer for this. We also attached our "previous products" so you can get an idea of the type of company we are.

Target Market(s)

Cheese lovers, people who like snacks, natural food eaters.

Industry/Entity Type

Dairy Farm

Font styles to use
Serif
Script

Colors
ffffff
cadf82
f04a50
85cae6

Requirements
Must have
• All the point in the product description
Nice to have
• The points at a minimum.
Should not have
• Everything is explained. Do not make it look cartoonish!

```html
<!DOCTYPE html>
<html lang="en">
<head>
<meta charset="utf-8">
<title>Bravolt Fresh Mozzarella – Label Set</title>
<link rel="stylesheet" href="https://fonts.googleapis.com/css2?family=Marcellus&family=Caveat+Brush&family=Tinos&display=swap">
<style>
  :root {
    --paper: #ffffff;
    --frame: #8a8a8a;
    --meadow-light: #eef6cf;
    --meadow: #cadf82;
    --banner: #2a2119;
    --gold: #e2a93b;
    --gold-line: #d9a23a;
    --brand-red: #e63a3f;
    --ink: #2b241c;
    --weight-red: #d8342b;
    --badge-green: #5e9a34;
    --sky-blue: #85cae6;
    --cream: #f1ecd9;
    --parsley: #6f8a3a;
    --tomato: #c0402e;
  }
  html, body {
    margin: 0;
    padding: 0;
    overflow: hidden;
    background: var(--paper);
  }
  .canvas {
    width: 1200px;
    height: 662px;
    box-sizing: border-box;
    border: 1px solid var(--frame);
    background: var(--paper);
    overflow: hidden;
  }
  .canvas svg { display: block; width: 100%; height: 100%; }
  .brand-name { font-family: "Marcellus", serif; fill: var(--brand-red); letter-spacing: 1px; }
  .product-name { font-family: "Marcellus", serif; fill: var(--paper); letter-spacing: 1px; }
  .flavour { font-family: "Caveat Brush", cursive; fill: var(--ink); }
  .claim { font-family: "Marcellus", serif; fill: var(--ink); }
  .net-weight { font-family: "Tinos", serif; fill: var(--weight-red); }
</style>
</head>
<body>
<div class="canvas">
<svg viewBox="0 0 1480 817" preserveAspectRatio="none" xmlns="http://www.w3.org/2000/svg">
  <defs>
    <radialGradient id="meadow-glow" cx="50%" cy="30%" r="70%">
      <stop offset="0" stop-color="var(--meadow-light)"/>
      <stop offset="1" stop-color="var(--meadow)"/>
    </radialGradient>
    <linearGradient id="farm-tones" x1="0" y1="0" x2="0" y2="1">
      <stop offset="0" stop-color="#c9553a"/>
      <stop offset="0.55" stop-color="#b8402f"/>
      <stop offset="1" stop-color="#5f9a3a"/>
    </linearGradient>
    <linearGradient id="cheese-tones" x1="0" y1="0" x2="1" y2="1">
      <stop offset="0" stop-color="var(--sky-blue)"/>
      <stop offset="0.25" stop-color="var(--cream)"/>
      <stop offset="0.6" stop-color="#d9d6b6"/>
      <stop offset="0.8" stop-color="var(--parsley)"/>
      <stop offset="1" stop-color="#cfc9a8"/>
    </linearGradient>
    <clipPath id="round-label-clip"><circle cx="419" cy="343" r="301"/></clipPath>
    <clipPath id="side-label-clip"><rect x="872" y="307" width="513" height="237"/></clipPath>
  </defs>

  <!-- Round lid label -->
  <g class="round-label" clip-path="url(#round-label-clip)">
    <rect x="110" y="40" width="620" height="610" fill="url(#meadow-glow)"/>
    <text class="brand-name" x="413" y="128" text-anchor="middle" font-size="40">BRAVOLT</text>

    <rect class="farm-scene" role="img" aria-label="Farm scene with red barn, silo, windmill and cows on rolling green hills"
          x="245" y="170" width="275" height="150" rx="10" fill="url(#farm-tones)"/>

    <path class="cheese-photo" role="img" aria-label="Bowl of marinated mozzarella balls with sun-dried tomato and parsley"
          d="M720,378 C610,388 470,430 410,510 C372,560 350,605 340,650 L730,650 L730,378 Z" fill="url(#cheese-tones)"/>

    <path class="name-banner" d="M130,300 C300,322 500,262 725,283 L725,398 C520,372 330,428 130,417 Z" fill="var(--banner)"/>
    <path d="M140,312 C300,333 500,273 715,294" fill="none" stroke="var(--gold-line)" stroke-width="2"/>
    <text class="product-name" x="427" y="382" text-anchor="middle" font-size="46" transform="rotate(-4 427 370)">FRESH MOZZARELLA</text>

    <g transform="rotate(-7 418 416)">
      <rect class="flavour-ribbon" x="297" y="392" width="244" height="46" fill="var(--gold)"/>
      <text class="flavour" x="419" y="423" text-anchor="middle" font-size="20">SUN-DRIED TOMATO &amp; PARSLEY</text>
    </g>

    <text class="claim" x="285" y="496" text-anchor="middle" font-size="31">ALL</text>
    <text class="claim" x="285" y="528" text-anchor="middle" font-size="31">NATURAL</text>
    <text class="net-weight" x="300" y="554" text-anchor="middle" font-size="13">NET WT. 12oz</text>
    <text class="net-weight" x="300" y="568" text-anchor="middle" font-size="13">340g</text>

    <circle class="organic-badge" cx="168" cy="256" r="17" fill="none" stroke="var(--badge-green)" stroke-width="2"/>
    <circle cx="168" cy="256" r="9" fill="var(--badge-green)"/>
    <circle class="kosher-badge" cx="662" cy="252" r="14" fill="none" stroke="var(--badge-green)" stroke-width="3"/>
  </g>

  <!-- Side label -->
  <g class="side-label" clip-path="url(#side-label-clip)">
    <rect x="872" y="307" width="513" height="237" fill="url(#meadow-glow)"/>
    <text class="claim" x="894" y="338" font-size="11">ALL NATURAL</text>
    <text class="brand-name" x="1115" y="370" text-anchor="middle" font-size="30">BRAVOLT</text>
    <circle class="organic-badge" cx="1360" cy="330" r="10" fill="none" stroke="var(--badge-green)" stroke-width="1.5"/>
    <circle cx="1360" cy="330" r="5" fill="var(--badge-green)"/>
    <circle class="kosher-badge" cx="1361" cy="358" r="8" fill="none" stroke="var(--badge-green)" stroke-width="2"/>

    <rect class="farm-scene" role="img" aria-label="Farm scene with red barn, silo and cow on green hills"
          x="878" y="420" width="185" height="124" rx="6" fill="url(#farm-tones)"/>

    <path class="cheese-photo" role="img" aria-label="Marinated mozzarella balls with sun-dried tomato and parsley"
          d="M1385,402 C1300,398 1200,438 1168,544 L1385,544 Z" fill="url(#cheese-tones)"/>

    <path class="name-banner" d="M978,418 C1100,420 1180,396 1290,406 L1290,458 C1180,446 1080,480 978,480 Z" fill="var(--banner)"/>
    <path d="M984,424 C1100,426 1180,402 1284,412" fill="none" stroke="var(--gold-line)" stroke-width="1"/>
    <text class="product-name" x="1140" y="460" text-anchor="middle" font-size="25" transform="rotate(-4 1140 452)">FRESH MOZZARELLA</text>

    <g transform="rotate(-7 1125 480)">
      <rect class="flavour-ribbon" x="1058" y="468" width="134" height="24" fill="var(--gold)"/>
      <text class="flavour" x="1125" y="485" text-anchor="middle" font-size="10.5">SUN-DRIED TOMATO &amp; PARSLEY</text>
    </g>

    <text class="net-weight" x="1126" y="523" text-anchor="middle" font-size="9">NET WT. 12oz</text>
    <text class="net-weight" x="1126" y="533" text-anchor="middle" font-size="9">340g</text>
  </g>
</svg>
</div>
</body>
</html>
```